female esthetician looking for an impact business card

I an an expert in skin care industry with high experience in NYC.I want my business card to look professional , an impact at first look. I do want a combination between white and gold . I believe the font will be great if is gold.. The Fonts are also important. MIRELA COSTANDI (SKIN CARE BOUTIQUE)

THIS SHOULD BE THE BUSINESS NAME, and should be placed on th eback of the card.
IN front m, the name MIRELA COSTANDI - ESTHETCIAN

BY APPOINTMENTS ONLY: 512.478.2936

Target Market(s)

HIGH END CLIENTELE

Contact Information for Business Card

iT WILL BE on a luxury paper. I neeed the wow feeling

Requirements
Should not have
• pictures

```html
<!DOCTYPE html>
<html lang="en">
<head>
<meta charset="utf-8">
<title>Mirela Costandi – Business Card</title>
<link rel="stylesheet" href="https://fonts.googleapis.com/css2?family=Cinzel:wght@500&family=Questrial&display=swap">
<style>
  :root {
    --page: #ffffff;
    --card-black: #0b0b0b;
    --card-charcoal: #1c1c1c;
    --pattern-grey: #2a2a2a;
    --gold: #d4a937;
    --gold-deep: #9c7418;
    --gold-light: #f0cf6a;
    --text-light: #e9e9e9;
    --text-muted: #bdbdbd;
  }
  * { box-sizing: border-box; margin: 0; padding: 0; }
  html, body {
    width: 1200px; height: 900px; overflow: hidden;
    background: var(--page);
  }
  .canvas {
    position: relative; width: 1200px; height: 900px;
  }
  .card {
    position: absolute; top: 300px;
    width: 540px; height: 310px;
    border-radius: 24px; overflow: hidden;
    box-shadow: 0 18px 40px rgba(0,0,0,0.18);
  }
  /* Front: business name */
  .card--front {
    left: 42px;
    background: var(--card-black);
  }
  .damask-field {
    position: absolute; inset: 0;
    background: radial-gradient(ellipse at 50% 45%, var(--pattern-grey) 0%, var(--card-charcoal) 45%, var(--card-black) 100%);
  }
  .ornament {
    position: absolute; left: 50%; transform: translateX(-50%);
    background: linear-gradient(180deg, var(--gold-light), var(--gold) 50%, var(--gold-deep));
    border-radius: 40px;
    opacity: 0.92;
  }
  .ornament--top { top: 62px; width: 180px; height: 62px; }
  .ornament--bottom { top: 196px; width: 160px; height: 62px; }
  .name-band {
    position: absolute; left: 0; right: 0; top: 134px; height: 56px;
    background: rgba(0,0,0,0.85);
    border-top: 2px solid var(--gold);
    border-bottom: 2px solid var(--gold);
    text-align: center;
  }
  .brand-name {
    font-family: "Cinzel", serif; font-weight: 500;
    font-size: 31px; line-height: 1; letter-spacing: 1px;
    color: var(--gold);
    margin-top: 5px;
  }
  .brand-tagline {
    font-family: "Questrial", sans-serif;
    font-size: 10px; letter-spacing: 5px;
    color: var(--gold);
    margin-top: 5px;
  }
  /* Back: contact */
  .card--back {
    left: 618px;
    background:
      repeating-linear-gradient(90deg, rgba(255,255,255,0.018) 0 14px, rgba(0,0,0,0) 14px 28px),
      radial-gradient(ellipse at 50% 45%, #2b2b2b 0%, #141414 55%, var(--card-black) 100%);
    text-align: center;
  }
  .contact {
    position: absolute; left: 0; right: 0; top: 100px;
  }
  .contact-name {
    font-family: "Cinzel", serif; font-weight: 500;
    font-size: 21px; letter-spacing: 0.5px;
    color: var(--gold);
    line-height: 1;
  }
  .contact-role {
    font-family: "Questrial", sans-serif;
    font-size: 9px; letter-spacing: 1px;
    color: var(--gold);
    margin-top: 3px;
  }
  .contact-note {
    font-family: "Questrial", sans-serif;
    font-size: 12px; letter-spacing: 0.5px;
    color: var(--text-muted);
    margin-top: 26px;
  }
  .contact-phone {
    font-family: "Questrial", sans-serif;
    font-size: 19px; letter-spacing: 1px;
    color: var(--text-light);
    margin-top: 3px;
  }
</style>
</head>
<body>
<main class="canvas">
  <section class="card card--front">
    <div class="damask-field" role="img" aria-label="Dark grey damask pattern across the card"></div>
    <div class="ornament ornament--top" role="img" aria-label="Gold baroque scroll ornament above the name"></div>
    <div class="ornament ornament--bottom" role="img" aria-label="Gold baroque scroll ornament below the name"></div>
    <div class="name-band">
      <h1 class="brand-name">MIRELA COSTANDI</h1>
      <p class="brand-tagline">SKIN CARE BOUTIQUE</p>
    </div>
  </section>

  <section class="card card--back">
    <div class="contact">
      <h2 class="contact-name">MIRELA COSTANDI</h2>
      <p class="contact-role">ESTHETCIAN</p>
      <p class="contact-note">BY APPOINTMENTS ONLY</p>
      <p class="contact-phone">512.478.2936</p>
    </div>
  </section>
</main>
</body>
</html>
```